Need a Poster for our Cricket Club(A2)

We need to get a Poster for advertisement to attract more Players( Junior/ Female & Senior Mens ) for our cricket club. i have attached our Club Logo as well Kids Program logo(Zesto Playstart Bat for ages 5-8 yrs)..We need emphasize more on Juniors & female Players

Our Club Logo have Navy & Gold so need those colors as part of the flyers..Also our Club Name is Wembury Falcons Cricket Club , based @

Tolbray Reserve,
48 Tolbray Ave,
Kestrel Park
VIC 3988

Contacts:

for Women's Cricket & Juniors put the contact details of

Ravi Pannu 0491 263 578 (Vice President Women Committee)
Harpreet Grewal 0438 152 669 (Secretary Women Committee)
Melanie Grewal 0417 395 826 (Captain Women's Cricket Team)
Tarun Bajwa 0409 672 143 (Juniors Coordinator)

for Senior Men's Cricket put the contact details of

Anand Kapoor 0402 718 390 (President)
Suresh Pannu 0436 204 851 (Vice President)
Nikhil Rao 0403 581 927 (Club Captain)

https://www.clubhuddle.net/WemburyFalcons/

These all names can be at the bottom of the Poster

Rest Let me know if you need anything else..

Thanks

Just little bit about club

Wembury Falcons Cricket Club is one of most respected clubs in northern suburbs. Since our establishment 8 years ago, we have won 6 premierships, stood runner up 3 times. There has never been an year in which one of the Falcons team, didn’t make it to final series.

We are based in Tolbray reserve, Tolbray av, Kestrel Park. Year by year we have grown and reached higher peaks.

Taking our success to newer heights, WFCC is introducing Women’s team into TVCL competitions in season 2017-18.

As the new season is approaching, we are now actively looking for players for our Senior/Junior/Women team to grow even further and help promote grass roots cricket

Target Market(s)

Cricket Community

Industry/Entity Type

Club

Requirements
Must have
• Emphasis on Women's & Juniors Cricket..
• Club's progress as strong Community Club

```html
<!DOCTYPE html>
<html lang="en">
<head>
<meta charset="utf-8">
<title>Wembury Falcons Cricket Club – Poster</title>
<link href="https://fonts.googleapis.com/css2?family=Alfa+Slab+One&family=Lato:wght@400;700;900&family=Open+Sans:wght@800&family=Roboto+Condensed:wght@600&display=swap" rel="stylesheet">
<style>
  :root {
    --navy: #12345f;
    --navy-deep: #0d2a4f;
    --gold: #d6b36a;
    --gold-deep: #b8903f;
    --teal: #1c6884;
    --teal-deep: #0f4c68;
    --white: #ffffff;
    --panel: rgba(18, 58, 98, 0.5);
    --bg: #e6e6e6;
  }
  * { margin: 0; padding: 0; box-sizing: border-box; }
  html, body { width: 1200px; height: 1200px; overflow: hidden; background: var(--bg); }
  .poster {
    position: absolute; left: 176px; top: 0; width: 848px; height: 1200px;
    overflow: hidden;
    background: linear-gradient(180deg, var(--teal) 40%, var(--teal-deep) 100%);
    font-family: "Lato", sans-serif; color: var(--white);
  }
  .stadium-photo {
    position: absolute; left: 0; top: 0; width: 848px; height: 440px;
    background: linear-gradient(180deg, #d9c7a4 0%, #f4efe2 28%, #9aa47a 52%, #6dbb3c 72%, #8fd24c 100%);
  }
  .player-silhouettes {
    position: absolute; left: 0; top: 440px; width: 848px; height: 760px;
    background: linear-gradient(90deg, rgba(10,40,60,0.35) 0%, rgba(10,40,60,0) 35%, rgba(10,40,60,0) 65%, rgba(10,40,60,0.35) 100%);
  }
  .frame { position: absolute; inset: 0; }
  .crest {
    position: absolute; left: 330px; top: 32px; width: 190px; height: 225px;
    display: flex; flex-direction: column; align-items: center; justify-content: center; gap: 10px;
  }
  .crest-mark { width: 28px; height: 28px; border-radius: 50%; background: var(--navy); }
  .crest-name { font-weight: 900; font-size: 20px; color: var(--navy); text-align: center; line-height: 1.15; }
  .welcome {
    position: absolute; left: 0; width: 848px; top: 282px; text-align: center;
    font-family: "Alfa Slab One", serif; font-size: 46px; line-height: 56px; color: var(--gold-deep); letter-spacing: 1px;
  }
  .welcome-to {
    position: absolute; left: 0; width: 848px; top: 344px; text-align: center;
    font-family: "Alfa Slab One", serif; font-size: 20px; line-height: 24px; color: #1a1a1a;
  }
  .club-name {
    position: absolute; left: 0; width: 848px; top: 378px; text-align: center;
    font-weight: 900; line-height: 1;
  }
  .club-name .line-top { display: block; font-size: 18px; letter-spacing: 22px; padding-left: 22px; color: var(--gold-deep); }
  .club-name .line-main { display: block; font-size: 58px; letter-spacing: 2px; color: var(--navy); margin-top: 4px; }
  .club-name .line-sub { display: block; font-size: 17px; letter-spacing: 14px; padding-left: 14px; color: var(--gold-deep); margin-top: 8px; }
  .kids-program {
    position: absolute; left: 680px; top: 528px; width: 118px; height: 180px;
    border-radius: 14px 14px 50px 50px; background: #5aa83a;
    display: flex; align-items: center; justify-content: center; text-align: center;
    font-weight: 900; font-size: 18px; line-height: 1.2; color: var(--white); padding: 10px;
  }
  .meet-heading {
    position: absolute; left: 0; width: 848px; top: 682px; text-align: center;
    font-family: "Open Sans", sans-serif; font-weight: 800; font-size: 23px;
  }
  .panel { position: absolute; background: var(--panel); text-align: center; }
  .address { left: 235px; top: 717px; width: 376px; height: 60px; padding-top: 8px;
    font-weight: 900; font-size: 17px; line-height: 22px; letter-spacing: 0.3px; }
  .contacts-women { left: 218px; top: 822px; width: 402px; height: 148px; padding-top: 12px; }
  .contacts-men { left: 260px; top: 990px; width: 330px; height: 128px; padding-top: 12px; }
  .panel-heading { font-family: "Roboto Condensed", sans-serif; font-weight: 600; font-size: 22px; margin-bottom: 14px; }
  .contact-list { list-style: none; font-size: 11.5px; line-height: 18.5px; }
  .contacts-men .contact-list { font-size: 12.5px; line-height: 20px; }
  .contact-list span { margin: 0 5px; }
  .social { position: absolute; left: 236px; top: 1140px; display: flex; align-items: center; gap: 14px; }
  .social-square { width: 34px; height: 34px; background: var(--white); border-radius: 5px; }
  .social-url { background: rgba(8, 20, 35, 0.85); padding: 3px 8px; font-size: 14.5px; }
</style>
</head>
<body>
<main class="poster">
  <div class="stadium-photo" role="img" aria-label="Cricket stadium at sunset with floodlights and green field"></div>
  <div class="player-silhouettes" role="img" aria-label="Silhouettes of a batsman and a young player batting"></div>

  <svg class="frame" width="848" height="1200" viewBox="0 0 848 1200" aria-hidden="true">
    <defs>
      <linearGradient id="silverEdge" x1="0" y1="0" x2="1" y2="0">
        <stop offset="0" stop-color="#8d9296"/><stop offset="0.5" stop-color="#f4f5f6"/><stop offset="1" stop-color="#9ea3a7"/>
      </linearGradient>
      <linearGradient id="shieldFill" x1="0" y1="0" x2="0" y2="1">
        <stop offset="0" stop-color="#f6f6f6"/><stop offset="0.6" stop-color="#c9cbcd"/><stop offset="1" stop-color="#9da1a5"/>
      </linearGradient>
    </defs>
    <path d="M0,280 C40,560 85,900 100,1200 L75,1200 C60,900 30,600 0,340 Z" fill="var(--gold)"/>
    <path d="M0,340 C30,600 60,900 75,1200 L0,1200 Z" fill="var(--navy)"/>
    <path d="M0,0 L30,0 C20,120 12,220 0,300 Z" fill="url(#silverEdge)"/>
    <path d="M10,330 Q110,385 180,425" stroke="var(--gold)" stroke-width="14" fill="none"/>
    <path d="M848,280 C808,560 763,900 748,1200 L773,1200 C788,900 818,600 848,340 Z" fill="var(--gold)"/>
    <path d="M848,340 C818,600 788,900 773,1200 L848,1200 Z" fill="var(--navy)"/>
    <path d="M848,0 L818,0 C828,120 836,220 848,300 Z" fill="url(#silverEdge)"/>
    <path d="M838,330 Q740,385 668,425" stroke="var(--gold)" stroke-width="14" fill="none"/>
    <path d="M333,40 Q425,22 517,40 L517,150 Q500,235 425,257 Q350,235 333,150 Z" fill="#ffffff" fill-opacity="0.85" stroke="var(--gold)" stroke-width="8"/>
    <path d="M118,412 Q425,300 738,428 Q745,440 730,450 Q560,520 430,628 Q425,634 420,628 Q300,520 122,430 Q110,420 118,412 Z" fill="url(#shieldFill)" stroke="#f0f0f0" stroke-width="4"/>
  </svg>

  <div class="crest">
    <span class="crest-mark"></span>
    <span class="crest-name">Wembury<br>Falcons</span>
  </div>

  <h1 class="welcome">WELCOME</h1>
  <p class="welcome-to">TO</p>
  <p class="club-name">
    <span class="line-top">WEMBURY</span>
    <span class="line-main">FALCONS</span>
    <span class="line-sub">CRICKET CLUB</span>
  </p>

  <div class="kids-program">Zesto Playstart Bat</div>

  <h2 class="meet-heading">COME MEET US AT</h2>
  <p class="panel address">Tolbray Reserve, 48 Tolbray Ave,<br>Kestrel Park VIC&nbsp;&nbsp;3988</p>

  <section class="panel contacts-women">
    <h3 class="panel-heading">FOR WOMENS AND JUNIORS CRICKET</h3>
    <ul class="contact-list">
      <li>Ravi Pannu<span>0491 263 578</span>(Vice President Women Committee)</li>
      <li>Harpreet Grewal<span>0438 152 669</span>(Secretary Women Committee)</li>
      <li>Melanie Grewal<span>0417 395 826</span>(Captain Women's Cricket Team)</li>
      <li>Tarun Bajwa<span>0409 672 143</span>(Juniors Coordinator)</li>
    </ul>
  </section>

  <section class="panel contacts-men">
    <h3 class="panel-heading">FOR SENIOR MEN'S CRICKET</h3>
    <ul class="contact-list">
      <li>Anand Kapoor<span>0402 718 390</span>(President)</li>
      <li>Suresh Pannu<span>0436 204 851</span>(Vice President)</li>
      <li>Nikhil Rao<span>0403 581 927</span>(Club Captain)</li>
    </ul>
  </section>

  <div class="social">
    <span class="social-square"></span>
    <span class="social-url">https://www.clubhuddle.net/WemburyFalcons/</span>
  </div>
</main>
</body>
</html>
```